Aerospace Private Equity Firm Needs Website

We need a website for new private equity fund called Corvin Partners. We buy smaller companies in the aerospace and industrial industries. I have attached some information about the firm. An example of a site we like that is a similar business but focused in a different sector is www.tarnowcare.com. www.quillstonefunds.com is a firm that also invests in aerospace companies.

Industry/Entity Type

Equity

Number of Pages Required

1 page

Colors
0555a3
33a6d7
ec1f27

```html
<!DOCTYPE html>
<html lang="en">
<head>
<meta charset="utf-8">
<title>Corvin Partners</title>
<link href="https://fonts.googleapis.com/css2?family=Open+Sans:wght@400;600;700&family=Quicksand:wght@500;600&display=swap" rel="stylesheet">
<style>
  :root {
    --navy: #0555a3;
    --sky: #33a6d7;
    --red: #ec1f27;
    --ink: #333333;
    --text: #555555;
    --muted: #8a8a8a;
    --rule: #dddddd;
    --concrete: #e4e4e4;
    --white: #ffffff;
  }
  * { box-sizing: border-box; margin: 0; padding: 0; }
  html, body { width: 1200px; height: 2230px; overflow: hidden; }
  body {
    position: relative;
    background: var(--white);
    font-family: "Open Sans", Arial, sans-serif;
    color: var(--text);
    font-size: 14.5px;
    line-height: 22px;
  }
  .heading { font-family: "Quicksand", "Trebuchet MS", sans-serif; font-weight: 500; color: var(--ink); }

  /* Header */
  .site-header { position: absolute; left: 0; top: 0; width: 1200px; height: 94px; }
  .brand { position: absolute; left: 112px; top: 30px; display: flex; align-items: center; gap: 7px; white-space: nowrap; }
  .brand-mark { width: 10px; height: 10px; background: var(--red); }
  .brand-name { font-family: "Open Sans", sans-serif; font-weight: 700; font-size: 19px; color: var(--navy); letter-spacing: -0.2px; }
  .main-nav { position: absolute; left: 321px; top: 36px; display: flex; gap: 23px; white-space: nowrap; }
  .main-nav a { font-size: 14px; font-weight: 600; color: #222; text-decoration: none; letter-spacing: 0.2px; }
  .header-actions { position: absolute; left: 922px; top: 10px; width: 166px; }
  .header-btn { display: flex; align-items: center; gap: 9px; height: 35px; padding-left: 16px; margin-bottom: 6px; color: var(--white); font-size: 13.5px; font-weight: 700; text-decoration: none; white-space: nowrap; }
  .header-btn.brochure { background: var(--navy); }
  .header-btn.login { background: var(--red); }

  /* Hero */
  .hero { position: absolute; left: 0; top: 94px; width: 1200px; height: 513px; }
  .hero-photo { width: 100%; height: 100%; background: linear-gradient(180deg, #5a5f66 0%, #8f8a7e 22%, #b9b2a1 40%, #6f8fa6 62%, #a9553a 80%, #6b6a63 100%); }
  .hero-banner { position: absolute; left: 0; top: 455px; width: 100%; height: 32px; background: var(--sky); color: var(--white); text-align: center; font-family: "Quicksand", sans-serif; font-weight: 600; font-size: 20px; line-height: 32px; }

  /* Intro */
  .intro { position: absolute; left: 112px; top: 656px; width: 978px; height: 215px; }
  .intro-col { position: absolute; top: 0; }
  .intro-col.welcome { left: 0; width: 445px; }
  .intro-col.strategy { left: 517px; width: 461px; }
  .intro-divider { position: absolute; left: 487px; top: 6px; width: 1px; height: 205px; background: var(--rule); }
  .intro h2 { font-size: 20px; margin-bottom: 13px; }
  .intro p { font-size: 14px; line-height: 22.5px; }
  .outline-btn { display: inline-block; border: 1px solid var(--sky); color: var(--sky); font-size: 11px; font-weight: 700; letter-spacing: 0.4px; padding: 0 12px; height: 34px; line-height: 32px; text-decoration: none; background: var(--white); white-space: nowrap; }
  .intro .outline-btn { margin-top: 15px; }

  /* Highlights */
  .highlights { position: absolute; left: 0; top: 920px; width: 1200px; height: 600px; background: var(--concrete); }
  .card { position: absolute; top: 52px; width: 308px; height: 496px; background: var(--white); }
  .card.criteria { left: 112px; }
  .card.team { left: 446px; }
  .card.news { left: 781px; }
  .card-head { height: 67px; padding-left: 26px; color: var(--white); font-family: "Quicksand", sans-serif; font-weight: 500; font-size: 20px; line-height: 67px; }
  .criteria .card-head { background: var(--navy); }
  .team .card-head { background: var(--sky); }
  .news .card-head { background: var(--red); }
  .card-list { list-style: none; padding: 15px 36px 0 38px; }
  .card-list li { position: relative; font-size: 13.5px; line-height: 22px; margin-bottom: 6px; }
  .card-list li::before { content: ""; position: absolute; left: -14px; top: 9px; width: 5px; height: 5px; background: #c4c4c4; transform: rotate(45deg); }
  .team .card-list li { margin-bottom: 21px; }
  .news-list { list-style: none; padding: 14px 24px 0 32px; }
  .news-list li { margin-bottom: 13px; }
  .news-date { display: block; font-size: 12px; color: var(--muted); line-height: 20px; }
  .news-title { display: block; font-size: 13.5px; font-weight: 700; color: #2a2a2a; line-height: 22px; }
  .card .outline-btn { position: absolute; left: 50%; transform: translateX(-50%); top: 436px; }

  /* Key factors */
  .key-factors { position: absolute; left: 112px; top: 1565px; width: 480px; }
  .key-factors h2 { font-size: 20px; margin-bottom: 14px; }
  .factor-col { position: absolute; top: 42px; width: 216px; list-style: none; }
  .factor-col.first { left: 0; }
  .factor-col.second { left: 249px; }
  .factor-col li { position: relative; padding-left: 16px; font-size: 13.5px; line-height: 22.5px; margin-bottom: 21px; }
  .factor-col li svg { position: absolute; left: 0; top: 8px; }
  .team-frame { position: absolute; left: 613px; top: 1572px; width: 474px; height: 532px; background: var(--sky); }
  .team-photo { position: absolute; left: 0; top: 9px; width: 465px; height: 523px; background: linear-gradient(160deg, #e9ecef 0%, #c9cdd3 35%, #8d8a86 60%, #2f3b55 85%, #1f2a44 100%); }

  /* Footer */
  .site-footer { position: absolute; left: 0; top: 2156px; width: 1200px; height: 74px; background: var(--navy); color: var(--white); }
  .legal { position: absolute; left: 112px; top: 24px; font-size: 12.5px; white-space: nowrap; }
  .legal a { color: var(--white); text-decoration: none; }
  .legal .sep { margin: 0 5px; }
  .footer-brand { position: absolute; right: 112px; top: 22px; font-weight: 700; font-size: 19px; color: var(--white); white-space: nowrap; }
</style>
</head>
<body>

<header class="site-header">
  <div class="brand"><span class="brand-mark"></span><span class="brand-name">Corvin Partners</span></div>
  <nav class="main-nav">
    <a href="#">OVERVIEW</a>
    <a href="#">INVESTMENT CRITERIA</a>
    <a href="#">TEAM</a>
    <a href="#">PORTFOLIO</a>
    <a href="#">NEWS</a>
    <a href="#">CONTACT</a>
  </nav>
  <div class="header-actions">
    <a class="header-btn brochure" href="#">
      <svg width="11" height="13" viewBox="0 0 11 13"><rect x="0.5" y="0.5" width="10" height="12" fill="none" stroke="#fff"/><rect x="2.5" y="3" width="6" height="3" fill="#fff"/></svg>
      FIRM BROCHURE
    </a>
    <a class="header-btn login" href="#">
      <svg width="13" height="13" viewBox="0 0 13 13"><rect x="0.7" y="0.7" width="11.6" height="11.6" rx="2" fill="none" stroke="#fff" stroke-width="1.4"/><path d="M3 6.5h6M6.5 4l2.5 2.5L6.5 9" fill="none" stroke="#fff" stroke-width="1.4"/></svg>
      INVESTOR LOGIN
    </a>
  </div>
</header>

<section class="hero">
  <div class="hero-photo" role="img" aria-label="Wide view of a large industrial machining hall with overhead cranes and numbered columns"></div>
  <div class="hero-banner">Lower Middle - Market Buyout Fund $200 Million Target, $250 Million Hard Cap</div>
</section>

<section class="intro">
  <div class="intro-col welcome">
    <h2 class="heading">Welcome to Corvin Partners</h2>
    <p>Corvin Partners (“Corvin”) is a Los Angeles, California - based private equity firm formed in 2016 by Principals from Bramwell Ridge Associates (BRA). Corvin focuses on lower middle - market control investments in aerospace and industrial companies based in North America. The Corvin team has invested successfully in these sectors over a 10 - year period while at BRA.</p>
    <a class="outline-btn" href="#">READ MORE</a>
  </div>
  <div class="intro-divider"></div>
  <div class="intro-col strategy">
    <h2 class="heading">Our Strategy</h2>
    <p>Corvin will invest in undervalued aerospace and industrial companies. Areas of focus will include metallic structures, fluid conveyance, composite structures and surface treatment companies. Industrial investments will target companies that share common characteristics with aerospace; namely, engineering - driven precision manufacturing with regulated quality controls and product certification requirements.</p>
    <a class="outline-btn" href="#">READ MORE</a>
  </div>
</section>

<section class="highlights">
  <article class="card criteria">
    <h3 class="card-head">Investment Criteria</h3>
    <ul class="card-list">
      <li>Value focused</li>
      <li>Family or entrepreneur- owned / Corporate carve - outs</li>
      <li>EBITDA up to $10mm</li>
      <li>Enterprise Value $20 - $100mm</li>
      <li>Deploy $10 - $25mm in equity per investment</li>
      <li>Profitable, stable, cash - flowing companies</li>
      <li>Opportunity for growth, strategic &amp; operational change</li>
      <li>Target 70% aerospace / 30% industrial</li>
    </ul>
    <a class="outline-btn" href="#">VIEW MORE</a>
  </article>
  <article class="card team">
    <h3 class="card-head">Our Team</h3>
    <ul class="card-list">
      <li>60 years of combined investing and operating experience</li>
      <li>Worked together for over 10 years completing over 30 platform and add - on investments</li>
      <li>Partners have led 14 platform investments, deploying $266mm generating2.7x gross MOIC*</li>
    </ul>
    <a class="outline-btn" href="#">VIEW MORE</a>
  </article>
  <article class="card news">
    <h3 class="card-head">News Updates</h3>
    <ul class="news-list">
      <li><span class="news-date">20 Jun 2017</span><span class="news-title">Nullam ac urna eu felis dapibus condimentum sit amet a augue.</span></li>
      <li><span class="news-date">20 Jun 2017</span><span class="news-title">Nullam ac urna eu felis dapibus condimentum sit amet a augue.</span></li>
      <li><span class="news-date">20 Jun 2017</span><span class="news-title">Nullam ac urna eu felis dapibus condimentum sit amet a augue.</span></li>
      <li><span class="news-date">20 Jun 2017</span><span class="news-title">Nullam ac urna eu felis dapibus condimentum sit amet a augue.</span></li>
    </ul>
    <a class="outline-btn" href="#">VIEW MORE</a>
  </article>
</section>

<section class="key-factors">
  <h2 class="heading">Key Factors</h2>
  <ul class="factor-col first">
    <li><svg width="8" height="7" viewBox="0 0 8 7"><path d="M1 3.5l2 2L7 1" fill="none" stroke="#33a6d7" stroke-width="1.6"/></svg>Aerospace is a large, growing global market that has historically outperformed the S&amp;P 500</li>
    <li><svg width="8" height="7" viewBox="0 0 8 7"><path d="M1 3.5l2 2L7 1" fill="none" stroke="#33a6d7" stroke-width="1.6"/></svg>Corvin strategically positioned – deep relationships with key suppliers and OEMs (Altair Aerostructures, Kestrel Dynamics, Harlan Systems, Meridian Power, Vantor Aeronautics)</li>
    <li><svg width="8" height="7" viewBox="0 0 8 7"><path d="M1 3.5l2 2L7 1" fill="none" stroke="#33a6d7" stroke-width="1.6"/></svg>Cost pressures at OEM’s are driving outsourced manufacturing</li>
    <li><svg width="8" height="7" viewBox="0 0 8 7"><path d="M1 3.5l2 2L7 1" fill="none" stroke="#33a6d7" stroke-width="1.6"/></svg>Multi- year diversified backlogs at OEM’s and long - term supply agreements – good visibility on top line</li>
    <li><svg width="8" height="7" viewBox="0 0 8 7"><path d="M1 3.5l2 2L7 1" fill="none" stroke="#33a6d7" stroke-width="1.6"/></svg>Robust pipeline – 5 actionable deals</li>
  </ul>
  <ul class="factor-col second">
    <li><svg width="8" height="7" viewBox="0 0 8 7"><path d="M1 3.5l2 2L7 1" fill="none" stroke="#33a6d7" stroke-width="1.6"/></svg>Preferred partner with OEMs – facilitates introductions to potential investments</li>
    <li><svg width="8" height="7" viewBox="0 0 8 7"><path d="M1 3.5l2 2L7 1" fill="none" stroke="#33a6d7" stroke-width="1.6"/></svg>Supply base to OEMs highly fragmented with significant barriers to entry</li>
    <li><svg width="8" height="7" viewBox="0 0 8 7"><path d="M1 3.5l2 2L7 1" fill="none" stroke="#33a6d7" stroke-width="1.6"/></svg>LMM underserved by PE firms and investment banks</li>
    <li><svg width="8" height="7" viewBox="0 0 8 7"><path d="M1 3.5l2 2L7 1" fill="none" stroke="#33a6d7" stroke-width="1.6"/></svg>Southern California – largest supply cluster in the world for aerospace and one of the largest manufacturing bases in the US – 1,700 companies in Corvin’s target market</li>
  </ul>
</section>

<div class="team-frame">
  <div class="team-photo" role="img" aria-label="Team of colleagues in an office raising hands together in a celebratory high five"></div>
</div>

<footer class="site-footer">
  <p class="legal">© 2017 Corvin Partners Fund I, L.P. <a href="#">Terms of Use</a><span class="sep">|</span><a href="#">Privacy</a><span class="sep">|</span><a href="#">Sitemap</a></p>
  <div class="footer-brand">Corvin Partners</div>
</footer>

</body>
</html>
```